Lumora aesthetics offers a range of facial aesthetics treatments by a fully qualified dentist, to a high end crowd. Treatments include antiwrinkle treatment, the use of dermal fillers to provide facial volumisation and rejuvenation and also lip volumisation.
I want a luxurious and bold look. Black background with a bold striking gold logo in the centre possibly incorporating the outline of a face in a subtle yet effective way. I want it to include the work I offer so people will be aware of what they are looking into but not look like there's too much on the card, So it's a clean look.
At the bottom I would like it to say by Dr. Meera Sandhu. Alongside my email address and mobile number.

```html
<!DOCTYPE html>
<html lang="en">
<head>
<meta charset="utf-8">
<title>Lumora Aesthetics – Business Card</title>
<link href="https://fonts.googleapis.com/css2?family=Cinzel:wght@400;500&family=Open+Sans:wght@400&display=swap" rel="stylesheet">
<style>
  :root {
    --page-bg: #e9e6e1;
    --card-black: #121212;
    --gold-text: #e0c07a;
    --gold-light: #f6e39a;
    --gold-mid: #c9a43e;
    --gold-dark: #8a6a1c;
  }
  * { margin: 0; padding: 0; box-sizing: border-box; }
  html, body {
    width: 1200px;
    height: 1000px;
    overflow: hidden;
    background: var(--page-bg);
  }
  .business-card {
    position: absolute;
    left: 150px;
    top: 231px;
    width: 900px;
    height: 538px;
    background: var(--card-black);
    box-shadow: 0 12px 30px rgba(0,0,0,0.25);
  }
  .brand-mark {
    position: absolute;
    left: 92px;
    top: 95px;
    width: 120px;
    height: 120px;
    border-radius: 50%;
    background: var(--gold-mid);
  }
  .brand-name {
    position: absolute;
    left: 240px;
    top: 122px;
    font-family: "Cinzel", serif;
    font-weight: 400;
    font-size: 50px;
    letter-spacing: 1px;
    color: var(--gold-text);
    line-height: 1;
    white-space: nowrap;
  }
  .practitioner {
    position: absolute;
    left: 243px;
    top: 262px;
    font-family: "Cinzel", serif;
    font-weight: 500;
    font-size: 29px;
    color: var(--gold-text);
    line-height: 1;
  }
  .contact-list {
    position: absolute;
    left: 243px;
    top: 318px;
    list-style: none;
    font-family: "Open Sans", sans-serif;
    font-size: 22px;
    color: var(--gold-text);
  }
  .contact-list li {
    display: flex;
    align-items: center;
    height: 35px;
  }
  .contact-list svg { margin-right: 10px; flex: none; }
  .treatments {
    position: absolute;
    left: 240px;
    top: 413px;
    font-family: "Open Sans", sans-serif;
    font-size: 22.5px;
    line-height: 32px;
    color: var(--gold-text);
    white-space: nowrap;
  }
  .gold-band {
    position: absolute;
    left: 0;
    bottom: 2px;
    width: 100%;
    height: 14px;
    background: linear-gradient(90deg, var(--gold-dark) 0%, var(--gold-mid) 25%, var(--gold-light) 55%, var(--gold-mid) 80%, var(--gold-dark) 100%);
  }
</style>
</head>
<body>
  <div class="business-card">
    <div class="brand-mark"></div>
    <div class="brand-name">LUMORA AESTHETICS</div>
    <div class="practitioner">DR. MEERA SANDHU</div>
    <ul class="contact-list">
      <li>
        <svg width="14" height="22" viewBox="0 0 14 22" aria-hidden="true">
          <rect x="1.5" y="1" width="11" height="20" rx="2" fill="none" stroke="#e0c07a" stroke-width="1.8"/>
          <line x1="5" y1="18" x2="9" y2="18" stroke="#e0c07a" stroke-width="1.5"/>
        </svg>
        + 000 000 0000
      </li>
      <li>
        <svg width="20" height="14" viewBox="0 0 20 14" aria-hidden="true">
          <rect x="0" y="0" width="20" height="14" fill="#e0c07a"/>
          <polyline points="0,0 10,8 20,0" fill="none" stroke="#121212" stroke-width="1.6"/>
        </svg>
        info@lumoraclinic.com
      </li>
    </ul>
    <p class="treatments">
      Frown Line • Crows feet • Bunny lines • Neck lines<br>
      Eyebrow lift Marionette lines • Hyperhidrosis
    </p>
    <div class="gold-band"></div>
  </div>
</body>
</html>
```